Letterhead

We would like to use the logo attached as a new letterhead. Our problem is that we think the dark blue background is too much. We'd like a sleek, professional letterhead, and we'd like at least five options to choose from. I've also uploaded our old letterhead for reference of the style we're going for.

```html
<!DOCTYPE html>
<html lang="en">
<head>
<meta charset="utf-8">
<title>Alder Row Strategies — Letterhead</title>
<link href="https://fonts.googleapis.com/css2?family=Arimo:wght@400;700&family=Tinos:wght@400&display=swap" rel="stylesheet">
<style>
  :root {
    --navy: #1c2d4f;
    --gold: #c5a467;
    --ink: #3a3a3a;
    --rule: #555555;
    --paper: #ffffff;
    --backdrop: #d9d9d9;
  }
  * { box-sizing: border-box; margin: 0; padding: 0; }
  html, body { width: 1200px; height: 1159px; overflow: hidden; }
  body { background: var(--backdrop); position: relative; }

  .sheet {
    position: absolute; left: 190px; top: 45px;
    width: 820px; height: 1070px;
    background: var(--paper);
    box-shadow: 0 6px 24px rgba(0,0,0,.18);
    overflow: hidden;
  }

  .brand {
    position: absolute; left: 70px; top: 118px;
    display: flex; align-items: center; gap: 14px;
  }
  .brand-mark { width: 30px; height: 30px; background: var(--gold); }
  .brand-name {
    font-family: "Tinos", serif; font-weight: 400;
    font-size: 30px; letter-spacing: 2px; line-height: 1;
    color: var(--navy); text-transform: uppercase;
  }

  .contact {
    position: absolute; right: 70px; top: 48px; width: 200px;
    font-family: "Tinos", serif; font-size: 12.5px; line-height: 1.35;
    color: var(--ink);
    padding-bottom: 6px; border-bottom: 1px solid var(--rule);
  }
  .contact-line { display: flex; align-items: center; gap: 6px; }
  .contact-line svg { width: 10px; height: 10px; flex: none; fill: var(--gold); }
  .contact-address { margin-bottom: 4px; }

  .header-rule {
    position: absolute; left: 70px; right: 70px; top: 190px;
    height: 1px; background: var(--rule);
  }

  .letter {
    position: absolute; left: 150px; right: 110px; top: 330px;
    font-family: "Arimo", sans-serif; color: var(--ink);
  }
  .salutation { font-weight: 700; font-size: 17px; margin-bottom: 18px; }
  .letter p { font-size: 13.5px; line-height: 1.3; margin-bottom: 22px; }
  .closing { font-weight: 700; font-size: 12px; margin-top: 36px; }

  .footer-bands {
    position: absolute; left: 0; bottom: 0; width: 820px; height: 40px;
  }
</style>
</head>
<body>
  <div class="sheet">
    <div class="brand">
      <span class="brand-mark"></span>
      <span class="brand-name">Alder Row Strategies</span>
    </div>

    <div class="contact">
      <div class="contact-address">Your Address, City<br>State, Zip 0000</div>
      <div class="contact-line">
        <svg viewBox="0 0 10 10"><path d="M2 0.5 L3.6 2.6 L2.8 3.6 Q4 6 6.4 7.2 L7.4 6.4 L9.5 8 L8.3 9.5 Q2.5 8.5 0.5 1.7 Z"/></svg>
        <span>044-123 456 789</span>
      </div>
      <div class="contact-line">
        <svg viewBox="0 0 10 10"><path d="M0.5 2 H9.5 V8 H0.5 Z M1 2.5 L5 5.5 L9 2.5" stroke="#fff" stroke-width="0.7"/></svg>
        <span>info@alderrow.example</span>
      </div>
      <div class="contact-line">
        <svg viewBox="0 0 10 10"><circle cx="5" cy="5" r="4.5"/></svg>
        <span>www.alderrow.example</span>
      </div>
    </div>

    <div class="header-rule"></div>

    <div class="letter">
      <div class="salutation">Dear Mr. Smith,</div>
      <p>Lorem ipsum dolor sit amet, consectetuer adipiscing elit, sed diam nonummy nibh euismod tincidunt ut laor eet dolore magna aliquam erat volutpat. Ut wisi enim ad minim veniam, quis nostrud exerci tationmcorper suscipit lobortis nisl ut aliquip ex ea commodo consequat. Duis autem vel eum iriure dolor in hendrerit in vulputate velit esse molestie consequat, vel illum dolore eu feugiat</p>
      <p>Rorem ipsum dolor sit amet, consectetuer adipiscing elit, sed diam nonummy nibh euismod tincidunt ut laor eet dolore magna aliquam erat volutpat. Ut wisi enim ad minim veniam, quis nostrud exerci tationmcorper suscipit lobortis nisl ut aliquip ex ea commodo consequat. Duis autem vel eum iriure dolor in hendrerit in vulputate velit esse molest</p>
      <p>Dorem ipsum dolor sit amet, consectetuer adipiscing elit, sed diam nonummy nibh euismod tincidunt ut laor eet dolore magna aliquam erat volutpat. Ut wisi enim ad minim veniam, quis nostrud exerci tationmcorper suscipit lobortis nisl ut aliquip ex ea commodo consequat. Duis autem vel eum iriure dolor in hendrerit in suscipit lobortis nisl ut aliquip ex ea commodo consequat. Duis autem vel eum iriure dolor in hendrerit in vulputate velit esse molestie consequat, vel illum</p>
      <p>Sorem ipsum dolor sit amet, consectetuer adipiscing elit, sed diam nonummy nibh euismod tincidunt ut laor eet dolore magna aliquam erat volutpat. Ut wisi enim ad minim veniam, quis nostrud exerci tationmcorper suscipit lobortis nisl ut aliquip ex ea commodo consequat. Duis autem vel eum iriure dolor in</p>
      <div class="closing">Sincerely,</div>
    </div>

    <svg class="footer-bands" viewBox="0 0 820 40" preserveAspectRatio="none" aria-hidden="true">
      <polygon points="0,28 640,28 628,40 0,40" fill="var(--navy)"/>
      <polygon points="652,28 820,0 820,40 640,40" fill="var(--gold)"/>
    </svg>
  </div>
</body>
</html>
```